Falvoreth Concert

i need envelope a4 size and normal size - folder -paper bag - business card -
letterhead

Stationery Design project 'Stationery falvoreth concrete : letterhead ,folder,business card ,envelope ,envelope A4size .paper bag '

Target Market(s)

ready mix concrete

Font styles to use
Serif

Colors

Designer to choose colors to be used in the design.

Requirements
Must have
• nice design

```html
<!DOCTYPE html>
<html lang="en">
<head>
<meta charset="utf-8">
<title>Falvoreth for Concrete – Business Card</title>
<link href="https://fonts.googleapis.com/css2?family=Open+Sans:wght@400;600&family=Noto+Naskh+Arabic:wght@400;700&display=swap" rel="stylesheet">
<style>
  :root {
    --brand-blue: #0b4d8c;
    --brand-blue-light: #2f6aa3;
    --paper: #ffffff;
    --ink: #1d1d1f;
    --backdrop: #e8ebee;
  }
  * { box-sizing: border-box; margin: 0; padding: 0; }
  html, body { width: 1200px; height: 846px; overflow: hidden; }
  body {
    background: var(--backdrop);
    font-family: "Open Sans", Arial, sans-serif;
    position: relative;
  }
  .card {
    position: absolute;
    top: 276px;
    width: 530px;
    height: 294px;
    box-shadow: 0 3px 10px rgba(0,0,0,0.12);
    overflow: hidden;
  }
  /* front */
  .card--front { left: 50px; background: var(--brand-blue); }
  .front-pattern {
    position: absolute; top: 0; right: 0;
    width: 300px; height: 130px;
    background: linear-gradient(135deg, var(--brand-blue-light), var(--brand-blue));
    opacity: 0.55;
  }
  .front-mark {
    position: absolute; left: 130px; top: 128px;
    display: flex; align-items: center; gap: 12px;
  }
  .front-mark .dot { width: 22px; height: 22px; border-radius: 50%; background: var(--paper); }
  .front-mark .name { color: var(--paper); font-weight: 600; font-size: 26px; letter-spacing: 0.5px; }

  /* back */
  .card--back { left: 620px; background: var(--paper); color: var(--ink); }
  .back-mark {
    position: absolute; left: 34px; top: 112px;
    display: flex; align-items: center; gap: 10px;
  }
  .back-mark .dot { width: 18px; height: 18px; border-radius: 50%; background: var(--brand-blue); }
  .back-mark .name { color: var(--brand-blue); font-weight: 600; font-size: 20px; }
  .tagline-ku {
    position: absolute; right: 30px; top: 26px;
    direction: rtl; text-align: right;
    font-family: "Noto Naskh Arabic", serif;
    line-height: 1.3;
  }
  .tagline-ku .company { color: var(--brand-blue); font-weight: 700; font-size: 22px; display: block; }
  .tagline-ku .service { color: var(--ink); font-size: 19px; display: block; }
  .holder {
    position: absolute; left: 34px; bottom: 26px;
    font-size: 12.5px; line-height: 1.45;
  }
  .holder .person { color: var(--brand-blue); font-size: 19px; font-weight: 400; }
  .contact {
    position: absolute; right: 26px; top: 118px;
    display: flex; align-items: flex-start; gap: 10px;
    font-size: 12.5px; text-align: right; line-height: 1.55;
  }
  .contact-icons {
    width: 22px; padding: 5px 0; border-radius: 11px;
    background: var(--brand-blue);
    display: flex; flex-direction: column; align-items: center; gap: 4px;
  }
  .contact-icons svg { width: 12px; height: 12px; }
  .web {
    position: absolute; right: 30px; bottom: 26px;
    font-size: 12.5px; text-align: right; line-height: 1.5;
  }
</style>
</head>
<body>

<section class="card card--front" aria-label="Business card front">
  <div class="front-pattern" role="img" aria-label="Faint repeated brand monogram pattern"></div>
  <div class="front-mark">
    <span class="dot"></span>
    <span class="name">Falvoreth for Concrete</span>
  </div>
</section>

<section class="card card--back" aria-label="Business card back">
  <div class="tagline-ku">
    <span class="company">کۆمپانیای فالڤۆرێس</span>
    <span class="service">بۆ کۆنکریتی ئامادەکراو</span>
  </div>

  <div class="back-mark">
    <span class="dot"></span>
    <span class="name">Falvoreth for Concrete</span>
  </div>

  <div class="contact">
    <div class="contact-lines">
      0770 555 0182<br>
      0 750 555 0347
    </div>
    <div class="contact-icons" aria-hidden="true">
      <svg viewBox="0 0 12 12"><path d="M3 1l2 2-1 1.5c.6 1.3 1.6 2.3 2.9 2.9L8.4 6.5l2 2L9.3 10.6C5.2 10.3 1.7 6.8 1.4 2.7z" fill="#fff"/></svg>
      <svg viewBox="0 0 12 12"><path d="M3 1l2 2-1 1.5c.6 1.3 1.6 2.3 2.9 2.9L8.4 6.5l2 2L9.3 10.6C5.2 10.3 1.7 6.8 1.4 2.7z" fill="#fff"/></svg>
      <svg viewBox="0 0 12 12"><rect x="1" y="2.5" width="10" height="7" fill="none" stroke="#fff" stroke-width="1.2"/><path d="M1 2.5l5 4 5-4" fill="none" stroke="#fff" stroke-width="1.2"/></svg>
      <svg viewBox="0 0 12 12"><circle cx="6" cy="6" r="4.8" fill="none" stroke="#fff" stroke-width="1.1"/><ellipse cx="6" cy="6" rx="2" ry="4.8" fill="none" stroke="#fff" stroke-width="1"/><path d="M1.2 6h9.6" stroke="#fff" stroke-width="1"/></svg>
    </div>
  </div>

  <div class="holder">
    <div class="person">Your Name</div>
    <div class="title">Title</div>
    <div>Behind Hawar Medical Center</div>
    <div>Azadi Street - Sulaimanya</div>
    <div>Kurdistan Region</div>
  </div>

  <div class="web">
    info@falvorethconcrete.com<br>
    www.falvorethconcrete.com
  </div>
</section>

</body>
</html>
```